Bertrand Music Video and Film Production

THE FLYER SHOULD INCLUDE THIS TEXT:

"PROFESSIONAL FILM AND MUSIC VIDEO DIRECTzOR WITH OVER 10 YEARS EXPERIENCE. CLIENT LIST INCLUDES, 518, MARDEWICK, QUEEN LANTERNS, BRACKENMOOR, THE PLOVERS, TAN FOG, DORA-MAE, JUNE FARROW, OVX, PINECONE.
HD, SUPER 8, LIVE DVD, PROMO REELS AND VIDEOS ON TIME AND ON BUDGET."

I need to create a flyer/ad that I will use to promote myself and the services I provide.

My name is Bertrand Kowalczyk and I am a music video clip director and editor that can achieve great results regardless of budgets.

Working with HD and Super 8 vintage film formats to achieve the look you want.

I am a Melbourne based film maker with a huge client list; 518, Mardewick, Queen Lanterns, June Farrow, Dora-Mae, Brackenmoor, The Plovers, Lionel Brabham, Pinecone Marketing, OVX and Dunmore City Council.

Black and white classic design. Clean and neat not too busy, almost minimal in a way. Incorpirate my initials to create a logo perhaps.

It needs to appeal and relate to various music genres including; rock, pop, soul, funk, country and folk as I make music videos for artists of many genres.

Feature my website:

www.clipvault-example.net/berkowal

Include my email address

bertrandkowalczyk@mailnest-example.net

Many thanks

Bertrand

Target Market(s)

Music artists and bands performing all sorts of music styles from; rock, soul, funk, pop, country and folk.

Appealing also to band managers, artist representation and record labels/music publishers.

Industry/Entity Type

Artists

Requirements
Must have
• My website and email address and my name. I am a sole trader so i don't have a business name as such, just my name, Bertrand Kowalczyk.
Should not have
• a picture of me

```html
<!DOCTYPE html>
<html lang="en">
<head>
<meta charset="utf-8">
<title>Bertrand Kowalczyk – Film and Music Video Director</title>
<link rel="stylesheet" href="https://fonts.googleapis.com/css2?family=Arvo:wght@700&family=Josefin+Sans:wght@300;700&display=swap">
<style>
  :root {
    --page: #2f333b;
    --flyer-centre: #434954;
    --flyer-edge: #262a31;
    --accent: #f55f5e;
    --accent-line: #d94c4c;
    --ink: #f2f2f2;
    --rule: #c9ccd2;
  }
  * { margin: 0; padding: 0; box-sizing: border-box; }
  html, body { width: 918px; height: 1200px; overflow: hidden; background: var(--page); }
  .flyer {
    position: relative;
    width: 918px;
    height: 1200px;
    overflow: hidden;
    background: radial-gradient(ellipse 80% 60% at 45% 35%, var(--flyer-centre), var(--flyer-edge));
    font-family: "Josefin Sans", "Helvetica Neue", Arial, sans-serif;
    color: var(--ink);
  }
  .name {
    position: absolute;
    left: 40px;
    right: 36px;
    top: 410px;
    font-family: "Arvo", "Rockwell", Georgia, serif;
    font-weight: 700;
    line-height: 1;
  }
  .name span {
    display: block;
    background: repeating-linear-gradient(to bottom, var(--accent) 0 3px, var(--accent-line) 3px 4px);
    -webkit-background-clip: text;
    background-clip: text;
    color: transparent;
  }
  .name-first { font-size: 92px; letter-spacing: -2px; }
  .name-last { font-size: 112px; letter-spacing: -3px; text-align: right; margin-top: -6px; text-transform: uppercase; }
  .silhouette {
    position: absolute;
    left: 236px;
    top: 540px;
    width: 230px;
    height: 260px;
    border-radius: 115px 115px 0 0;
    background: linear-gradient(to bottom, #2c3037 0%, #343943 55%, rgba(58, 63, 73, 0) 100%);
  }
  .services {
    position: absolute;
    right: 92px;
    top: 632px;
    width: 440px;
    text-align: right;
    text-transform: uppercase;
    font-weight: 300;
    font-size: 20px;
    line-height: 27px;
  }
  .services p + p { margin-top: 18px; }
  .services strong { font-weight: 700; }
  .rule {
    position: absolute;
    left: 18px;
    right: 94px;
    top: 1062px;
    border-top: 2px dashed var(--rule);
  }
  .contact {
    position: absolute;
    left: 12px;
    right: 12px;
    top: 1128px;
    text-align: center;
    font-weight: 700;
    font-size: 15px;
    letter-spacing: 2px;
    text-transform: uppercase;
    white-space: nowrap;
  }
  .contact .divider { color: var(--accent); margin: 0 8px; }
</style>
</head>
<body>
  <main class="flyer">
    <h1 class="name">
      <span class="name-first">Bertrand</span>
      <span class="name-last">Kowalczyk</span>
    </h1>
    <div class="silhouette" role="img" aria-label="Dark silhouette of a head rising over the surname"></div>
    <section class="services">
      <p><strong>Professional</strong> film and music<br>video director with over 10<br>years experience.</p>
      <p><strong>Client list</strong> includes, 518,<br>Mardewick, Queen Lanterns,<br>Brackenmoor, The Plovers, Tan<br>Fog, Dora-Mae, June Farrow, OVX,<br>Pinecone.</p>
      <p><strong>HD, Super 8, Live DVD,</strong> promo<br>reels and videos on time and<br>on budget.</p>
    </section>
    <div class="rule"></div>
    <footer class="contact">
      <span>www.clipvault-example.net/berkowal</span><span class="divider">|</span><span>bertrandkowalczyk@mailnest-example.net</span>
    </footer>
  </main>
</body>
</html>
```